Website Development for stormbrookvault.com.au

Build a new Wordpress/Responsive website for stormbrookvault.com.au

Target Market(s)

Compliance Managers, Risk Managers, Information Security and Cyber Security Professionals, Chief Data/Digital Officers, Chief Operating/Financial Officers, Business Continuity Professionals, Disaster Recovery Planners, Small Business Owners, Local/Federal Government entities

Industry/Entity Type

Data Service

Coding

Coded - Design and coding required

Number of Pages Required

5+ page

Font styles to use
Sans Serif

Colors

Designer to choose colors to be used in the design.

Requirements
Must have
• 1. Site Structure: Home Page plus the following chapter-pages for a) Services b) About c) Resources d) Blog e) Contact Us
• 2. Prefer site to built on wordpress and we can purchase a theme if needed (we currently use Kelo4 for other sites)
• 3. Blog needs to be wordpress based
• 4. We will host the site ourselves on our own servers
• 5. Responsive Design
Nice to have
• 1. Livechat capability/interface
• 2. Capability for marketing automation integration (such as pinwhirl, flarevo, quillbranchly etc)
• 3. Capability for CRM integration (Tidewarden)

```html
<!DOCTYPE html>
<html lang="en">
<head>
<meta charset="utf-8">
<title>Stormbrook Vault</title>
<link href="https://fonts.googleapis.com/css2?family=Poppins:wght@300;400;500;600;700&family=Roboto:wght@300;400;500;700&display=swap" rel="stylesheet">
<style>
:root{
  --red:#e31b23;
  --navy:#0b1626;
  --navy-2:#17273d;
  --ink:#1c1c1c;
  --text:#555;
  --grey-bg:#ececec;
  --dark:#12141c;
  --white:#fff;
}
*{box-sizing:border-box;margin:0;padding:0}
html,body{width:1200px;height:4276px;overflow:hidden}
body{font-family:'Poppins',sans-serif;color:var(--ink);background:var(--white);position:relative}
.abs{position:absolute}
section,header,footer{position:absolute;left:0;width:1200px}

/* header */
.site-header{top:0;height:140px;background:var(--white)}
.brand{left:145px;top:38px;display:flex;align-items:center;gap:12px}
.brand-mark{width:34px;height:34px;border-radius:50%;background:var(--red)}
.brand-name{font-family:'Roboto',sans-serif;font-weight:700;font-size:34px;color:var(--red);letter-spacing:.5px}
.call{left:545px;top:24px;display:flex;align-items:center;gap:10px}
.call-icon{width:36px;height:36px;border-radius:50%;border:2px solid var(--red);display:flex;align-items:center;justify-content:center}
.call small{display:block;font-size:15px;color:var(--ink)}
.call strong{display:block;font-size:20px;color:var(--red);font-weight:600;line-height:1}
.search{left:790px;top:30px;width:265px;height:36px;border:1px solid #bbb;border-radius:18px;font-size:12px;color:#888;padding:10px 18px}
.search svg{position:absolute;right:14px;top:11px}
.main-nav{left:460px;top:96px;display:flex;gap:0}
.main-nav a{font-size:14px;font-weight:500;color:var(--ink);text-decoration:none;margin-right:30px}

/* hero */
.hero{top:140px;height:640px}
.hero-title{top:185px;width:100%;text-align:center;color:var(--white);font-size:72px;font-weight:300}
.hero-title b{font-weight:700}
.hero-sub{top:282px;width:100%;text-align:center;color:#dfe6ee;font-size:17px;line-height:30px}
.btn-red{background:var(--red);color:var(--white);font-weight:600;font-size:16px;border-radius:22px;text-align:center}
.hero .btn-red{left:510px;top:373px;width:180px;height:44px;line-height:44px}
.dots{top:548px;left:562px;display:flex;gap:5px}
.dots i{width:12px;height:12px;border-radius:50%;border:2px solid var(--white)}
.dots i:first-child{background:var(--white)}

/* headings */
.sec-title{font-size:38px;font-weight:700;text-transform:uppercase;color:var(--ink)}
.sec-title span{color:var(--red);font-weight:500}
.rule{width:62px;height:3px;background:var(--red)}
.para{font-size:14px;line-height:30px;color:var(--text)}
.btn-out{border:2px solid #333;border-radius:20px;font-size:14px;font-weight:600;text-align:center;width:142px;height:40px;line-height:36px}

/* about */
.about{top:780px;height:596px}

/* services */
.services{top:1376px;height:748px;background:var(--grey-bg)}
.svc{width:260px}
.svc h3{font-size:18px;font-weight:500;color:var(--ink);margin-bottom:6px}
.svc p{font-size:13px;line-height:22px;color:var(--text)}
.svc.left{text-align:right}
.svc-icon{width:64px;height:64px;border-radius:50%;background:var(--white);box-shadow:0 2px 6px rgba(0,0,0,.12);display:flex;align-items:center;justify-content:center}

/* resources */
.resources{top:2124px;height:586px}

/* blog */
.blog{top:2710px;height:820px;background:linear-gradient(#f1f1f1,#e2e4e6)}
.card{width:275px;height:370px;background:var(--white);box-shadow:0 3px 10px rgba(0,0,0,.12)}
.card-media{width:275px;height:195px}
.date{left:10px;top:10px;width:50px;height:46px;background:var(--red);color:var(--white);font-size:13px;font-weight:600;line-height:18px;padding:5px 6px}
.card h4{position:absolute;top:212px;left:20px;width:235px;text-align:center;font-size:19px;font-weight:400;color:#223;line-height:28px}
.card p{position:absolute;top:280px;left:25px;width:225px;text-align:center;font-size:13px;line-height:22px;color:var(--text)}

/* contact */
.contact{top:3530px;height:746px;background:var(--dark)}
.contact-title{top:55px;width:100%;text-align:center;color:var(--white);font-size:38px;font-weight:700}
.contact-title span{font-weight:400}
.info{left:145px;display:flex;gap:20px;color:var(--white);font-size:14px;line-height:22px}
.info-icon{width:50px;height:50px;border-radius:50%;background:var(--white);display:flex;align-items:center;justify-content:center;flex:none}
.field{border:1px solid #8a8d96;height:40px;color:#ccc;font-size:12px;padding:12px 10px;width:258px}
.social{width:34px;height:34px;border-radius:50%;border:2px solid var(--white)}
.chat-badge{left:928px;top:512px;width:140px;height:56px;background:var(--white);color:#000;font-family:'Roboto',sans-serif;font-weight:700;font-size:24px;text-align:center;line-height:56px}
.foot-brand{left:145px;top:590px;display:flex;align-items:center;gap:12px}
.foot-brand .brand-mark{width:44px;height:44px;background:var(--white)}
.foot-brand .brand-name{color:var(--white);font-size:38px}
.foot-nav{right:145px;top:612px;color:var(--white);font-size:16px}
.copyright{right:145px;top:652px;color:var(--white);font-size:15px}
</style>
</head>
<body>

<header class="site-header">
  <div class="abs brand"><span class="brand-mark"></span><span class="brand-name">Stormbrook Vault</span></div>
  <div class="abs call">
    <span class="call-icon"><svg width="18" height="18" viewBox="0 0 24 24"><path fill="#e31b23" d="M6.6 10.8a15 15 0 0 0 6.6 6.6l2.2-2.2a1 1 0 0 1 1-.25 11.4 11.4 0 0 0 3.6.57 1 1 0 0 1 1 1V20a1 1 0 0 1-1 1A17 17 0 0 1 3 4a1 1 0 0 1 1-1h3.5a1 1 0 0 1 1 1c0 1.25.2 2.45.57 3.57a1 1 0 0 1-.25 1z"/></svg></span>
    <div><small>Call Now</small><strong>+999 5548 2207</strong></div>
  </div>
  <div class="abs search">Search here
    <svg width="14" height="14" viewBox="0 0 24 24"><circle cx="10" cy="10" r="7" fill="none" stroke="#555" stroke-width="2.5"/><path d="M15 15l6 6" stroke="#555" stroke-width="2.5"/></svg>
  </div>
  <nav class="abs main-nav"><a>HOME</a><a>ABOUT US</a><a>OUR SERVICES</a><a>RESOURCES</a><a>BLOG</a><a>CONTACT</a></nav>
</header>

<section class="hero">
  <svg class="abs" style="left:0;top:0" width="1200" height="640" role="img" aria-label="Dark blue digital security backdrop with glowing hexagon grid and padlock symbols">
    <defs>
      <radialGradient id="heroGlow" cx="50%" cy="35%" r="70%">
        <stop offset="0" stop-color="#2a4360"/><stop offset=".6" stop-color="#111d2e"/><stop offset="1" stop-color="#070c15"/>
      </radialGradient>
    </defs>
    <polygon points="0,0 1200,0 1200,560 1070,580 868,595 600,660 333,590 150,600 0,575" fill="url(#heroGlow)"/>
    <polyline points="0,575 150,600 333,590 600,660 868,595 1070,580 1200,560" fill="none" stroke="#cfd6de" stroke-width="1"/>
    <circle cx="333" cy="590" r="13" fill="#fff" stroke="#e31b23" stroke-width="3"/>
    <circle cx="600" cy="660" r="14" fill="#fff" stroke="#e31b23" stroke-width="3"/>
    <circle cx="868" cy="595" r="13" fill="#fff" stroke="#e31b23" stroke-width="3"/>
  </svg>
  <h1 class="abs hero-title"><b>Stormbrook</b> Vault</h1>
  <p class="abs hero-sub">Nemo enim ipsam voluptatem quia voluptas sit aspernatur aut<br>odit aut fugit, sed quia consequuntur magni</p>
  <div class="abs btn-red">LEARN MORE</div>
  <div class="abs dots"><i></i><i></i><i></i><i></i></div>
</section>

<section class="about">
  <svg class="abs" style="left:145px;top:100px" width="370" height="420">
    <polygon points="185,4 364,107 364,313 185,416 6,313 6,107" fill="none" stroke="#e31b23" stroke-width="4"/>
    <polygon role="img" aria-label="Photo of a person working at computer monitors in an office" points="185,20 350,115 350,305 185,400 20,305 20,115" fill="#8a949e"/>
  </svg>
  <h2 class="abs sec-title" style="left:577px;top:105px">About <span>Stormbrook Vault</span></h2>
  <p class="abs para" style="left:577px;top:200px;width:480px">Sed ut perspiciatis unde omnis iste natus error sit voluptatem accusantium doloremque laudantium, totam rem aperiam, eaque ipsa quae ab illo inventore veritatis et quasi architecto beatae vitae dicta sunt explicabo. Nemo enim ipsam voluptatem quia voluptas sit aspernatur aut odit aut fugit lda totam rem aperiam</p>
  <p class="abs para" style="left:577px;top:370px;width:480px">Sed ut perspiciatis unde omnis iste natus error sit voluptatem accantium doloremque laudantium, totam rem aperiam, eaque ipsa quae</p>
  <div class="abs btn-out" style="left:577px;top:458px">READ MORE</div>
</section>

<section class="services">
  <svg class="abs" style="left:0;top:0" width="1200" height="20"><polygon points="510,0 690,0 600,20" fill="#fff"/></svg>
  <h2 class="abs sec-title" style="left:0;width:1200px;text-align:center;top:92px">Our Services</h2>
  <div class="abs rule" style="left:569px;top:165px"></div>
  <svg class="abs" style="left:400px;top:250px" width="400" height="400">
    <circle cx="200" cy="200" r="194" fill="#fff" stroke="#e31b23" stroke-width="2" stroke-dasharray="6 5"/>
  </svg>
  <div class="abs" style="left:460px;top:425px;width:280px;text-align:center;font-family:'Roboto',sans-serif;font-weight:700;font-size:30px;color:var(--red);line-height:38px">Stormbrook<br>Vault</div>

  <div class="abs svc left" style="left:118px;top:264px"><h3>Risk Management</h3><p>Sed ut perspiciatis unde omnis iste natus error sit voluptatem accusantium doloremque laudantium</p></div>
  <div class="abs svc left" style="left:78px;top:400px"><h3>Information Security</h3><p>Sed ut perspiciatis unde omnis iste natus error sit voluptatem accusantium doloremque</p></div>
  <div class="abs svc left" style="left:133px;top:536px"><h3>Cyber Security</h3><p>Sed ut perspiciatis unde omnis iste natus error sit voluptatem accusantium doloremque laudantium</p></div>
  <div class="abs svc" style="left:820px;top:264px"><h3>Disaster Recovery</h3><p>Sed ut perspiciatis unde omnis iste natus error sit voluptatem accusantium doloremque laudantium</p></div>
  <div class="abs svc" style="left:862px;top:400px"><h3>Business Continuity</h3><p>Sed ut perspiciatis unde omnis iste natus error sit voluptatem accusantium doloremque</p></div>
  <div class="abs svc" style="left:808px;top:536px"><h3>Financial</h3><p>Sed ut perspiciatis unde omnis iste natus error sit voluptatem accusantium doloremque laudantium</p></div>

  <div class="abs svc-icon" style="left:403px;top:272px"><svg width="30" height="30" viewBox="0 0 24 24" fill="none" stroke="#333" stroke-width="1.6"><path d="M12 3v18M6 21h12M4 9h16M6 9l-3 6h6zM18 9l-3 6h6z"/></svg></div>
  <div class="abs svc-icon" style="left:362px;top:408px"><svg width="30" height="30" viewBox="0 0 24 24" fill="none" stroke="#333" stroke-width="1.6"><path d="M12 2l8 3v6c0 5-3.5 9-8 11-4.5-2-8-6-8-11V5z"/><rect x="9" y="11" width="6" height="5"/><path d="M10 11V9a2 2 0 0 1 4 0v2"/></svg></div>
  <div class="abs svc-icon" style="left:418px;top:545px"><svg width="30" height="30" viewBox="0 0 24 24" fill="none" stroke="#333" stroke-width="1.6"><rect x="9" y="2" width="6" height="5"/><rect x="2" y="16" width="6" height="5"/><rect x="16" y="16" width="6" height="5"/><path d="M12 7v5M5 16v-4h14v4"/></svg></div>
  <div class="abs svc-icon" style="left:728px;top:272px"><svg width="30" height="30" viewBox="0 0 24 24" fill="none" stroke="#333" stroke-width="1.6"><rect x="3" y="4" width="18" height="12"/><path d="M8 20h8M12 16v4M8 10l3 3 5-5"/></svg></div>
  <div class="abs svc-icon" style="left:773px;top:408px"><svg width="30" height="30" viewBox="0 0 24 24" fill="none" stroke="#333" stroke-width="1.6"><circle cx="12" cy="10" r="5"/><path d="M4 21h16M7 21v-3h10v3M12 7v3l2 1"/></svg></div>
  <div class="abs svc-icon" style="left:713px;top:545px"><svg width="30" height="30" viewBox="0 0 24 24" fill="none" stroke="#333" stroke-width="1.6"><circle cx="8" cy="9" r="5"/><path d="M8 6v6M6 8h3a1 1 0 0 1 0 2H7"/><rect x="13" y="14" width="8" height="7"/><path d="M3 21h8"/></svg></div>
</section>

<section class="resources">
  <h2 class="abs sec-title" style="left:145px;top:105px">Resources</h2>
  <div class="abs rule" style="left:145px;top:175px"></div>
  <p class="abs para" style="left:145px;top:210px;width:480px">Sed ut perspiciatis unde omnis iste natus error sit voluptatem accusantium doloremque laudantium, totam rem aperiam, eaque ipsa quae ab illo inventore veritatis et quasi architecto beatae vitae dicta sunt explicabo. Nemo enim ipsam voluptatem quia voluptas sit aspernatur aut odit aut fugit lda totam rem aperiam totam rem aperiam, eaque ipsa quae ab illo inventore veritatis et quasi</p>
  <div class="abs btn-out" style="left:145px;top:436px">READ MORE</div>
  <svg class="abs" style="left:690px;top:80px" width="370" height="420">
    <polygon points="185,4 364,107 364,313 185,416 6,313 6,107" fill="none" stroke="#e31b23" stroke-width="4"/>
    <defs><linearGradient id="resGrad" x1="0" y1="0" x2="1" y2="1"><stop offset="0" stop-color="#c47a8e"/><stop offset=".5" stop-color="#3d4f8c"/><stop offset="1" stop-color="#1b2750"/></linearGradient></defs>
    <polygon role="img" aria-label="Photo of hands reviewing financial charts on a glowing screen" points="185,20 350,115 350,305 185,400 20,305 20,115" fill="url(#resGrad)"/>
  </svg>
</section>

<section class="blog">
  <svg class="abs" style="left:0;top:0" width="1200" height="60"><polygon points="0,0 1200,0 1200,10 690,10 600,60 510,10 0,10" fill="#fff"/></svg>
  <h2 class="abs sec-title" style="left:0;width:1200px;text-align:center;top:98px">Our Blog</h2>
  <div class="abs rule" style="left:569px;top:170px"></div>

  <article class="abs card" style="left:143px;top:235px">
    <div class="card-media" role="img" aria-label="Photo of wooden blocks stacked on a desk" style="background:linear-gradient(135deg,#d9b37a,#8d7458)"></div>
    <div class="abs date">Oct 01<br>2019</div>
    <h4>Sed ut perspiciatis unde omnis iste natus</h4>
    <p>Sed ut perspiciatis unde omnis iste natus sit voluptatem accusantium domque laudantium, totam</p>
  </article>
  <article class="abs card" style="left:460px;top:235px">
    <div class="card-media" role="img" aria-label="Photo of hands typing on a laptop" style="background:linear-gradient(135deg,#5f6670,#23272e)"></div>
    <div class="abs date">Oct 01<br>2019</div>
    <h4>Sed ut perspiciatis unde omnis iste natus</h4>
    <p>Sed ut perspiciatis unde omnis iste natus sit voluptatem accusantium domque laudantium, totam</p>
  </article>
  <article class="abs card" style="left:777px;top:235px">
    <div class="card-media" role="img" aria-label="Photo of a person working on a laptop at a bright desk" style="background:linear-gradient(135deg,#c5ced6,#7f8b96)"></div>
    <div class="abs date">Oct 01<br>2019</div>
    <h4>Sed ut perspiciatis unde omnis iste natus</h4>
    <p>Sed ut perspiciatis unde omnis iste natus sit voluptatem accusantium domque laudantium, totam</p>
  </article>
</section>

<section class="contact">
  <svg class="abs" style="left:0;top:-10px" width="1200" height="50">
    <polygon points="0,0 1200,0 1200,10 1090,10 1070,25 900,18 770,40 600,15 420,35 280,15 140,22 100,10 0,10" fill="#e2e4e6"/>
    <polyline points="0,10 100,10 140,22 280,15 420,35 600,15 770,40 900,18 1070,25 1090,10 1200,10" fill="none" stroke="#e31b23" stroke-width="6"/>
  </svg>
  <h2 class="abs contact-title">CONTACT <span>US</span></h2>
  <div class="abs rule" style="left:569px;top:125px"></div>

  <div class="abs info" style="top:170px"><span class="info-icon"><svg width="20" height="20" viewBox="0 0 24 24"><path fill="#12141c" d="M12 2a7 7 0 0 0-7 7c0 5 7 13 7 13s7-8 7-13a7 7 0 0 0-7-7zm0 9.5A2.5 2.5 0 1 1 12 6.5a2.5 2.5 0 0 1 0 5z"/></svg></span><div>Stormbrook Vault<br>42 Larkspur Lane<br>Halewood Vale HV4 7QT</div></div>
  <div class="abs info" style="top:257px"><span class="info-icon"><svg width="20" height="20" viewBox="0 0 24 24"><path fill="#12141c" d="M6.6 10.8a15 15 0 0 0 6.6 6.6l2.2-2.2a1 1 0 0 1 1-.25 11.4 11.4 0 0 0 3.6.57 1 1 0 0 1 1 1V20a1 1 0 0 1-1 1A17 17 0 0 1 3 4a1 1 0 0 1 1-1h3.5a1 1 0 0 1 1 1c0 1.25.2 2.45.57 3.57a1 1 0 0 1-.25 1z"/></svg></span><div>Phone :<br>877-555-0142</div></div>
  <div class="abs info" style="top:330px"><span class="info-icon"><svg width="20" height="20" viewBox="0 0 24 24" fill="none" stroke="#12141c" stroke-width="2"><rect x="7" y="2" width="10" height="20" rx="2"/><path d="M11 18h2"/></svg></span><div>Fax :<br>877-555-0187</div></div>
  <div class="abs info" style="top:400px"><span class="info-icon"><svg width="20" height="20" viewBox="0 0 24 24"><path fill="#12141c" d="M3 5h18v14H3zm2 2v.5l7 5 7-5V7l-7 5z"/></svg></span><div>Email :<br>info@stormbrookvault.com.au</div></div>

  <div class="abs field" style="left:520px;top:175px">Your Name</div>
  <div class="abs field" style="left:797px;top:175px">Your Email</div>
  <div class="abs field" style="left:520px;top:235px">Your Phone/Mobile</div>
  <div class="abs field" style="left:797px;top:235px">Subject</div>
  <div class="abs field" style="left:520px;top:300px;width:535px;height:100px">Your Message</div>
  <div class="abs btn-red" style="left:520px;top:423px;width:175px;height:38px;line-height:38px;border-radius:0;font-size:14px">SEND MESSAGES</div>
  <div class="abs social" style="left:713px;top:425px"></div>
  <div class="abs social" style="left:755px;top:425px"></div>
  <div class="abs social" style="left:797px;top:425px"></div>

  <div class="abs chat-badge">Talk Now</div>

  <div class="abs foot-brand"><span class="brand-mark"></span><span class="brand-name">Stormbrook Vault</span></div>
  <div class="abs foot-nav">Home &nbsp;| &nbsp;Services &nbsp;| &nbsp;About &nbsp;| &nbsp;Resources &nbsp;| &nbsp;Blog &nbsp;| &nbsp;Contact</div>
  <div class="abs copyright">Stormbrook Vault © 2019 All Rights Reserved</div>
</section>

</body>
</html>
```